Catering company looking to promote business

We need a flyer design for our company named "Peel and Pulp." We cater/deliver açaí bowls and smoothies.

The objective of this flyer is to let companies know that we are taking açaí bowls and smoothie orders and they can be delivered to them.

Some key points we would like on the flyer:
- Photo of açaí bowl and smoothie
- Menu w/ pricing
- "No hidden delivery fees"
- 5 bowl or smoothie minimum
- Online ordering through website:
https://tillbox.example/shop/peelandpulp
- For the month of February --> Get one free topping and drizzle!
- FRIDAY DELIVERIES ONLY
- Questions? Call (555) 730-9182
- social media friendwall & snapreel @pnpulp
- website www.peelandpulp.example

font - hello beautiful

Target Market(s)

Juice, smoothies, açaí bowls

Industry/Entity Type

Business

Font styles to use
Other font styles liked:
• Hello Beautiful

Colors
a64599
b768aa
d3a5cc
eedced
f7f1f7
9bcb3c

Requirements
Must have
• Please match logo, fonts, color schemes, etc.

```html
<!DOCTYPE html>
<html lang="en">
<head>
<meta charset="utf-8">
<title>Peel and Pulp – Açaí Delivery Flyer</title>
<link rel="stylesheet" href="https://fonts.googleapis.com/css2?family=Caveat+Brush&family=Montserrat:wght@400;500&display=swap">
<style>
  :root {
    --plum: #5e3591;
    --plum-deep: #4a2878;
    --orchid: #a64599;
    --mauve: #b768aa;
    --lilac: #d3a5cc;
    --blush: #eedced;
    --mist: #f7f1f7;
    --leaf: #9bcb3c;
    --white: #ffffff;
    --page: #ece8ee;
  }
  * { box-sizing: border-box; margin: 0; padding: 0; }
  html, body { width: 1200px; height: 800px; overflow: hidden; }
  body {
    background: var(--page);
    font-family: "Montserrat", Arial, sans-serif;
    display: flex; align-items: center; justify-content: center;
  }
  .flyer {
    position: relative;
    width: 600px; height: 776px;
    overflow: hidden;
    box-shadow: 0 6px 22px rgba(40, 20, 60, .25);
    color: var(--white);
  }
  .hero-photo {
    position: absolute; inset: 0;
    background:
      radial-gradient(ellipse at 62% 28%, #b3453f 0%, #7a2a2c 28%, transparent 55%),
      radial-gradient(ellipse at 80% 55%, #c9c3c0 0%, transparent 40%),
      linear-gradient(135deg, #3a302c 0%, #5a4a43 45%, #6e5850 100%);
  }
  .top-rule { position: absolute; top: 0; left: 0; right: 0; height: 8px; background: var(--orchid); }

  .brand {
    position: absolute; left: 38px; top: 52px;
    display: flex; align-items: center; gap: 12px;
  }
  .brand-ring {
    width: 118px; height: 118px; border-radius: 50%;
    border: 4px solid var(--orchid);
    display: flex; align-items: center; justify-content: center;
  }
  .brand-name {
    font-family: "Caveat Brush", cursive;
    font-size: 36px; line-height: .95; color: var(--mauve);
    text-align: center;
  }

  .order {
    position: absolute; left: 46px; top: 230px;
    font-family: "Caveat Brush", cursive; text-transform: uppercase;
  }
  .order-title { font-size: 38px; letter-spacing: 1px; }
  .order-link { font-size: 14px; line-height: 1.05; margin-top: 4px; }
  .order-handle { font-size: 24px; line-height: 1; }
  .questions { margin-top: 22px; }
  .questions-label { font-family: "Montserrat", sans-serif; font-size: 17px; letter-spacing: 1px; }
  .questions-phone { font-size: 24px; line-height: 1; }

  .menu-item {
    position: absolute; right: 36px;
    width: 172px; height: 172px; border-radius: 50%;
    border: 7px solid var(--mauve);
    overflow: hidden;
  }
  .menu-item.bowl { top: 30px; }
  .menu-item.smoothie { top: 218px; }
  .menu-photo { position: absolute; inset: 0; }
  .bowl .menu-photo { background: radial-gradient(circle at 50% 38%, #c2283c 0%, #7b2d4f 45%, #3b2a30 100%); }
  .smoothie .menu-photo { background: radial-gradient(circle at 45% 55%, #5c1f3a 0%, #7a6a62 55%, #cfc6c3 100%); }
  .menu-label {
    position: absolute; left: 0; right: 0; bottom: 22px;
    padding-left: 48px;
    font-family: "Caveat Brush", cursive; text-transform: uppercase;
    text-align: center; font-size: 20px; line-height: .95;
  }

  .wave { position: absolute; left: 0; bottom: 0; width: 600px; height: 360px; }

  .headline {
    position: absolute; left: 0; right: 0; top: 450px;
    font-family: "Caveat Brush", cursive; font-weight: 400; text-align: center;
    transform: rotate(-4deg);
  }
  .headline-lead { font-size: 56px; line-height: 1; }
  .headline-tail { font-size: 44px; text-transform: uppercase; line-height: 1; }

  .delivery-note {
    position: absolute; left: 30px; top: 602px;
    width: 250px; height: 66px;
  }
  .delivery-note svg { position: absolute; inset: 0; }
  .delivery-note p {
    position: relative; text-align: center; color: var(--white);
    font-family: "Caveat Brush", cursive; text-transform: uppercase;
  }
  .delivery-days { font-size: 22px; padding-top: 10px; line-height: 1; }
  .delivery-fees { font-size: 14px; line-height: 1.1; }

  .website {
    position: absolute; left: 44px; top: 694px;
    font-family: "Caveat Brush", cursive; text-transform: uppercase;
    font-size: 22px; letter-spacing: .5px;
  }

  .promo { position: absolute; left: 306px; top: 608px; width: 286px; }
  .promo-text {
    font-family: "Caveat Brush", cursive; text-transform: uppercase;
    font-size: 16px; line-height: 1.1;
  }
  .promo-text strong { font-weight: 400; font-size: 19px; display: block; white-space: nowrap; }
  .promo-min { font-size: 12px; margin-top: 8px; }

  .social { display: flex; gap: 28px; margin-top: 18px; font-size: 12px; }
  .social-item { display: flex; align-items: center; gap: 7px; }
  .social-mark {
    width: 14px; height: 14px; border-radius: 50%;
    border: 2px solid var(--lilac);
  }
</style>
</head>
<body>
  <article class="flyer">
    <div class="hero-photo" role="img" aria-label="Close-up photo of an açaí bowl topped with strawberries and granola"></div>
    <div class="top-rule"></div>

    <div class="brand">
      <div class="brand-ring"><span class="brand-name">Peel and<br>Pulp</span></div>
    </div>

    <section class="order">
      <p class="order-title">Order now!</p>
      <p class="order-link">Visit our online shop at:<br>https://tillbox.example/shop/</p>
      <p class="order-handle">peelandpulp</p>
      <div class="questions">
        <p class="questions-label">QUESTIONS?</p>
        <p class="questions-phone">Call (555) 730-9182</p>
      </div>
    </section>

    <figure class="menu-item bowl">
      <div class="menu-photo" role="img" aria-label="Photo of an açaí bowl held in a hand"></div>
      <figcaption class="menu-label">Açaí bowl<br>$9.00</figcaption>
    </figure>
    <figure class="menu-item smoothie">
      <div class="menu-photo" role="img" aria-label="Photo of a berry smoothie cup held in a hand"></div>
      <figcaption class="menu-label">Smoothie<br>$9.00</figcaption>
    </figure>

    <svg class="wave" viewBox="0 0 600 360" preserveAspectRatio="none" aria-hidden="true">
      <path d="M0 120 C 140 30, 360 10, 600 40 L600 60 C 380 40, 160 60, 0 150 Z" fill="var(--mauve)"/>
      <path d="M0 150 C 160 60, 380 40, 600 60 L600 360 L0 360 Z" fill="var(--plum)"/>
    </svg>

    <h1 class="headline">
      <span class="headline-lead">we deliver açaí bowl</span><br>
      <span class="headline-tail">directly to you!</span>
    </h1>

    <div class="delivery-note">
      <svg viewBox="0 0 250 66" preserveAspectRatio="none" aria-hidden="true">
        <path d="M12 20 C 80 4, 180 2, 244 8 L236 30 L248 40 C 170 48, 90 58, 6 64 L20 44 Z" fill="var(--lilac)"/>
      </svg>
      <p class="delivery-days">Friday deliveries only</p>
      <p class="delivery-fees">No hidden delivery fees</p>
    </div>

    <p class="website">www.peelandpulp.example</p>

    <section class="promo">
      <p class="promo-text">For the month of February<strong>Get one free topping and drizzle!</strong></p>
      <p class="promo-min">5 bowl or smoothie minimum</p>
      <div class="social">
        <span class="social-item"><span class="social-mark"></span>PnPulp</span>
        <span class="social-item"><span class="social-mark"></span>pnpulp</span>
      </div>
    </section>
  </article>
</body>
</html>
```